Charged by courts for driving with suspended license

To be seen by judges and lawyers. Would like some consistency between the brochures which is why we have used same images in places.

Target Market(s)

Lawyers, judges

Industry/Entity Type

legal, auto

Font styles to use
Sans Serif

Requirements
Nice to have
• I like the gears graphic I have used, but open to other ideas. Should be less industrial/automotive rather reflect mentally changing gears as clients need to change driving behaviour
Should not have
• images with manufacturers names etc. Maybe not have bright colours that are fun or summery as this si for judges, legal profession and must be serious, professional and stately

```html
<!DOCTYPE html>
<html lang="en">
<head>
<meta charset="utf-8">
<title>Changing Gears – Trifold Brochure</title>
<link rel="stylesheet" href="https://fonts.googleapis.com/css2?family=Montserrat:wght@400;500;600;700;800&display=swap">
<style>
  :root{
    --blue:#1f4f9f;
    --navy:#1d3f8a;
    --green:#6cb33f;
    --white:#ffffff;
    --ink:#2a2f3a;
    --muted:#9fb3d6;
    --page:#e9eaec;
    --tan:#b98a57;
  }
  *{box-sizing:border-box;margin:0;padding:0}
  html,body{width:1200px;height:2400px;overflow:hidden;background:var(--page)}
  body{font-family:"Montserrat",Arial,sans-serif;color:var(--ink)}
  .canvas{position:relative;width:1200px;height:2400px;overflow:hidden;background:var(--page)}

  .spread{position:absolute;left:50px;width:1100px;height:775px;background:var(--white);overflow:hidden;border-bottom:5px solid var(--green)}
  .spread--outside{top:200px}
  .spread--inside{top:1220px}

  .photo{position:absolute}
  .shapes{position:absolute;inset:0;width:1100px;height:775px}
  .panels{position:absolute;inset:0;display:grid;grid-template-columns:repeat(3,1fr)}
  .panel{position:relative;padding:0 24px}

  /* Outside spread */
  .background{color:var(--white);padding-top:26px}
  .background h2{color:var(--green);font-size:18px;font-weight:700;margin-bottom:24px}
  .background p{font-size:12.4px;line-height:1.62;text-align:justify;margin-bottom:26px}

  .motto{position:absolute;top:70px;left:0;right:0;text-align:center;color:var(--white);font-weight:700;font-size:22px;line-height:1.2}
  .motto li{list-style:none;margin-bottom:18px;text-shadow:0 1px 4px rgba(0,0,0,.45)}
  .brand{font-weight:700;color:var(--blue);text-align:center;line-height:1.05}
  .contact{position:absolute;top:490px;left:0;right:0;text-align:center}
  .contact .brand{font-size:30px;margin-bottom:40px}
  .contact h3{color:var(--blue);font-size:23px;font-weight:700;margin-bottom:34px}
  .contact .phone{color:var(--blue);font-size:25px;font-weight:700;margin-bottom:10px}
  .contact .web{color:var(--green);font-size:17px;font-weight:700;margin-bottom:6px}
  .contact .mail{color:var(--green);font-size:15px;font-weight:700}

  .cover{position:absolute;top:505px;left:0;right:0;text-align:center}
  .cover .brand{font-size:24px;margin-bottom:18px}
  .cover .title{font-weight:800;font-size:46px;line-height:1;letter-spacing:.5px}
  .cover .title span{display:block}
  .cover .title .t1{color:var(--navy)}
  .cover .title .t2{color:var(--green)}
  .cover .sub{color:var(--green);font-size:13px;font-weight:500;margin:14px 0 10px;line-height:1.3}
  .cover .charge{color:var(--navy);font-size:21px;font-weight:700;line-height:1.25}

  /* Inside spread */
  .inside h2{font-size:16px;font-weight:700;line-height:1.2}
  .inside h3{font-size:13.5px;font-weight:700;margin:14px 0 6px}
  .inside .lead{font-size:11px;margin:8px 0 8px}
  .inside ol{list-style:upper-roman;padding-left:24px;font-size:11px;line-height:1.3}
  .inside li{margin-bottom:5px;padding-left:4px}
  .inside li::marker{color:inherit}

  .course{padding-top:168px;color:var(--white)}
  .course h2{color:var(--white)}
  .course .accent{color:var(--green);font-size:13.5px;font-weight:700;margin-top:2px}
  .course .lead{color:var(--muted)}
  .course h3{color:var(--green)}

  .physiology{padding-top:196px}
  .physiology h2{color:var(--navy);font-size:14.5px}
  .physiology h3{color:var(--blue)}
  .physiology .note{color:var(--green);font-size:11px;font-weight:600;line-height:1.25;margin-bottom:10px}
  .physiology ol{color:var(--ink)}

  .habits{padding-top:320px}
  .habits ol{color:var(--ink)}
  .habits h2{color:var(--blue);font-size:17px;text-align:center;margin:14px 0 6px}

  .with-thumb{display:flow-root}
  .thumb{float:right;width:80px;height:80px;border-radius:50%;border:3px solid var(--white);box-shadow:0 2px 6px rgba(0,0,0,.3);margin:0 0 6px 10px}
  .thumb--rage{margin-top:-8px;background:radial-gradient(circle at 40% 40%,#dbe6f2,#5a86b8 70%,#2f5d91)}
  .thumb--context{margin-top:-40px;background:radial-gradient(circle at 45% 40%,#eef0f2,#a9b2bb 70%,#6d7782)}

  .remote{position:relative;width:238px;height:252px;margin:0 auto;background:var(--tan)}
  .remote .offer{position:absolute;right:12px;top:14px;color:var(--white);font-weight:800;font-size:18px;line-height:1.1;text-align:right}
  .remote .art{position:absolute;left:16px;right:16px;top:70px;height:128px;background:linear-gradient(135deg,#e6d2b6,#c9a77c)}
  .remote .cost{position:absolute;left:14px;right:14px;bottom:12px;height:24px;background:var(--white);display:flex;align-items:center;justify-content:center;gap:8px;font-size:10px;font-weight:700;color:var(--ink)}
  .remote .cost span{background:var(--ink);color:var(--white);padding:2px 6px;border-radius:3px;font-size:8.5px}
</style>
</head>
<body>
<main class="canvas">

  <section class="spread spread--outside">
    <div class="photo" style="left:366.67px;top:0;width:366.67px;height:470px;background:linear-gradient(160deg,#8fa3b8,#4d5b6b 60%,#2e3944)" role="img" aria-label="Photo of a driver giving a thumbs up from behind the wheel"></div>
    <div class="photo" style="left:733.33px;top:0;width:366.67px;height:480px;background:linear-gradient(160deg,#cfd9e4,#7d97b3 55%,#2f5f9a)" role="img" aria-label="Photo of a smiling student driver shaking hands with her instructor in a car"></div>

    <svg class="shapes" viewBox="0 0 1100 775" aria-hidden="true">
      <defs>
        <linearGradient id="paperOut" x1="0" y1="0" x2="0" y2="1">
          <stop offset="0" stop-color="#ffffff"/>
          <stop offset="1" stop-color="#eef0f3"/>
        </linearGradient>
      </defs>
      <path d="M366.67,410 C480,372 600,382 733.33,422 C850,458 980,472 1100,382 L1100,775 L366.67,775 Z" fill="url(#paperOut)"/>
      <path d="M366.67,396 C480,358 600,368 733.33,408 C850,444 980,458 1100,368" fill="none" stroke="#1f4f9f" stroke-width="14"/>
      <path d="M366.67,410 C480,372 600,382 733.33,422 C850,458 980,472 1100,382" fill="none" stroke="#6cb33f" stroke-width="7"/>
      <rect x="0" y="0" width="366.67" height="775" fill="#1f4f9f"/>
    </svg>

    <div class="panels">
      <article class="panel background">
        <h2>Our Background:</h2>
        <p>Since its inception in 1998, Lane Guide Driving School has strived to help drivers maintain their driving independence while leading safe and productive lives. Our motto “making drivers safe for life” drives our vision of helping drivers across industries and at all stages of our driving careers.</p>
        <p>Lane Guide started out working with school boards to deliver driver training to beginner drivers. Thousands of students have graduated from our ministry-approved curriculum. We are also ministry-approved to instruct defensive driving (DDC) and driver improvement courses (DIC), for drivers with speeding tickets, demerit points and at fault crashes.</p>
        <p>Lane Guide has also evolved to provide comprehensive driver rehabilitation to those who have lost, or are at risk of losing their license for medical reasons. This includes mobility issues requiring adaptive equipment, as well as traumatic crashes resulting in cognitive impairments and PTSD. We work with clients before the courts charged with impaired driving (alcohol, cannabis, opioids), road rage and stunt driving.</p>
        <p>Founder Martin Carter started driving at an early age on his parent’s farm. Driving professionally and doing so safely is in his DNA. Martin has a degree in Business and Psychology from Northvale University and is a certified in-car and in-class driving instructor</p>
      </article>

      <article class="panel">
        <ul class="motto">
          <li>• Maintaining</li>
          <li>• Driving independence,</li>
          <li>• while leading</li>
          <li>• Safe and productive<br>lives!</li>
        </ul>
        <div class="contact">
          <p class="brand">Lane Guide<br>Driving School</p>
          <h3>For more information:</h3>
          <p class="phone">705-555-0143</p>
          <p class="web">www.laneguidedriving.ca</p>
          <p class="mail">mcarter@laneguidedriving.ca</p>
        </div>
      </article>

      <article class="panel">
        <div class="cover">
          <p class="brand">Lane Guide<br>Driving School</p>
          <h1 class="title"><span class="t1">CHANGING</span><span class="t2">GEARS</span></h1>
          <p class="sub">A 1-DAY EDUCATIONAL COURSE<br>FOR THOSE CHARGED WITH</p>
          <p class="charge">DRIVING ON A<br>SUSPENDED LICENCE</p>
        </div>
      </article>
    </div>
  </section>

  <section class="spread spread--inside inside">
    <div class="photo" style="left:0;top:0;width:366.67px;height:200px;background:linear-gradient(160deg,#e8d6b8,#a88a62 55%,#3d4a58)" role="img" aria-label="Photo of a young woman driving a car"></div>
    <div class="photo" style="left:366.67px;top:0;width:366.67px;height:300px;background:linear-gradient(160deg,#c9d3dc,#6c7a88 55%,#2f3944)" role="img" aria-label="Photo of a frustrated driver gesturing angrily at the wheel"></div>
    <div class="photo" style="left:733.33px;top:0;width:366.67px;height:330px;background:linear-gradient(160deg,#f2f3f5,#9aa4ae 55%,#3b4048)" role="img" aria-label="Photo of an instructor pointing at a clipboard beside a driver at the wheel"></div>

    <svg class="shapes" viewBox="0 0 1100 775" aria-hidden="true">
      <defs>
        <linearGradient id="paperIn" x1="0" y1="0" x2="0" y2="1">
          <stop offset="0" stop-color="#ffffff"/>
          <stop offset="1" stop-color="#f1f2f4"/>
        </linearGradient>
        <clipPath id="firstPanel"><rect x="0" y="0" width="366.67" height="775"/></clipPath>
      </defs>
      <path d="M0,150 C120,128 250,130 366.67,142 C480,154 600,175 733.33,235 C830,280 950,300 1100,220 L1100,775 L0,775 Z" fill="url(#paperIn)"/>
      <path d="M0,150 C120,128 250,130 366.67,142 C480,154 600,175 733.33,235 C830,280 950,300 1100,220 L1100,775 L0,775 Z" fill="#1f4f9f" clip-path="url(#firstPanel)"/>
      <path d="M0,138 C120,116 250,118 366.67,130 C480,142 600,163 733.33,223 C830,268 950,288 1100,208" fill="none" stroke="#1f4f9f" stroke-width="10"/>
      <path d="M0,146 C120,124 250,126 366.67,138 C480,150 600,171 733.33,231 C830,276 950,296 1100,216" fill="none" stroke="#6cb33f" stroke-width="6"/>
    </svg>

    <div class="panels">
      <article class="panel course">
        <h2>SUSPENDED LICENCE -<br>CHANGING GEARS</h2>
        <p class="accent">During the course we will:</p>
        <p class="lead">Defensive Driving module (The Big 4):</p>
        <ol>
          <li>Lane position (better to drop 2 wheels on the shoulder than hit an oncoming vehicle)</li>
          <li>Following distance (varies depending on speed and conditions); space cushion driving (always have an out)</li>
          <li>Defensive stopping (what should we do every time we apply brakes?)</li>
          <li>Strategic driving / what we do with our eyes:</li>
        </ol>
        <h3>Law:</h3>
        <ol>
          <li>Highway Traffic Act (privilege vs right); Federal &amp; Provincial; ways we can lose our license</li>
          <li>Implications of a criminal record (relationships, work, financial)</li>
        </ol>
        <h3>Road Rage:</h3>
        <div class="with-thumb">
          <div class="thumb thumb--rage" role="img" aria-label="Round photo of an angry driver in a car"></div>
          <ol>
            <li>Defining the continuum of road rage and escalation of anger</li>
            <li>Triggers</li>
            <li>Personality types (Type A); Holmes &amp; Rahe stress scale</li>
          </ol>
        </div>
        <ol start="4">
          <li>Aggressive driving (overlap between aggressors and victims); reframing our views</li>
          <li>Psychiatric issues/PTSD: Not uncommon to have professional drivers come through the course due to over-exposure to stress from driving (both on the job and/or the commute to their driving job)</li>
        </ol>
      </article>

      <article class="panel physiology">
        <h2>Physiology of<br>aggressive driving and<br>how it affects the body:</h2>
        <ol style="margin-top:12px">
          <li>Window of tolerance (hyper-arousal vs hypo-arousal)</li>
          <li>Fight or flight response: how it works</li>
          <li>Stress hormones (Adrenaline, Cortisol, Norepinephrine)</li>
          <li>Chronic levels of exposure/Immune system suppression</li>
          <li>Hypertension</li>
          <li>Sympathetic nervous system</li>
          <li>Substances - will do an overview of alcohol/drinking and driving if relevant; individual and general factors that contribute to B.A.C</li>
        </ol>
        <h3>Personal context</h3>
        <div class="with-thumb">
          <div class="thumb thumb--context" role="img" aria-label="Round photo of an instructor beside a driver"></div>
          <p class="note">(risk vs protective factors);<br>incumbent upon us to consider:</p>
          <ol>
            <li>Genetics<br>(chemical predispositions)</li>
            <li>Socialization (role models)</li>
            <li>Environment</li>
          </ol>
        </div>
        <h3>Strategies to manage:</h3>
        <ol>
          <li>Stages of change theory; habit formation and how to reprogram (many of our decisions on any day are subconscious i.e., no decision-making process)</li>
        </ol>
      </article>

      <article class="panel habits">
        <ol start="2">
          <li>Neuroplasticity and habit formation</li>
          <li>Supernormal stimuli: how our bodies have not kept up to the complexities of today’s society and its stresses</li>
          <li>Ensure cerebral part of brain is making decisions and not “lizard” part of brain (amygdala vs cerebrum and their roles in the body); triggers &amp; stressors</li>
        </ol>
        <h2>COURSES ARE ONE-ON-ONE</h2>
        <div class="remote">
          <p class="offer">OFFERED<br>REMOTELY!</p>
          <div class="art" role="img" aria-label="Illustration of an online lesson with a presenter, a screen and learning icons"></div>
          <p class="cost"><span>Course Cost:</span>$775.00 + HST</p>
        </div>
      </article>
    </div>
  </section>

</main>
</body>
</html>
```